Commercial Construction Company

We need a business card design based on our current logo. We are a commercial general contractor based in Southern California that specializes in bank remodels. We would like to see designs that incorporate dark blue. The final design should portray an image of professionalism and quality.

If possible, I would like to add metallic foil to the design. Thank you

```html
<!DOCTYPE html>
<html lang="en">
<head>
<meta charset="utf-8">
<title>Halewood Business Card</title>
<link href="https://fonts.googleapis.com/css2?family=Quicksand:wght@400;500;700&display=swap" rel="stylesheet">
<style>
  :root {
    --navy: #1b2a52;
    --grey: #8f8f8f;
    --text-grey: #8a8a8a;
    --paper: #f1f1f1;
    --card-white: #fbfbfb;
    --card-black: #07090a;
    --gold: #b8912d;
  }
  html, body {
    margin: 0;
    padding: 0;
    width: 1200px;
    height: 1200px;
    overflow: hidden;
    background: var(--paper);
    font-family: "Quicksand", sans-serif;
  }
  .canvas { position: relative; width: 1200px; height: 1200px; }
  .card {
    position: absolute;
    left: 227px;
    width: 746px;
    height: 425px;
    box-shadow: 0 10px 24px rgba(0,0,0,0.18);
  }
  .card-front { top: 135px; background: var(--card-white); }
  .card-back { top: 639px; background: var(--card-black); }

  .side-band { position: absolute; left: 0; top: 0; width: 32px; height: 425px; }

  .brand {
    position: absolute;
    left: 74px;
    top: 95px;
    display: flex;
    align-items: center;
    gap: 12px;
  }
  .brand-dot { width: 22px; height: 22px; border-radius: 50%; background: var(--navy); }
  .brand-name {
    font-weight: 700;
    font-size: 44px;
    letter-spacing: 2px;
    color: var(--navy);
  }

  .person { position: absolute; left: 73px; right: 0; top: 240px; }
  .person-name {
    font-weight: 700;
    font-size: 22px;
    letter-spacing: 2px;
    color: var(--navy);
    margin: 0;
  }
  .title-row {
    display: flex;
    align-items: center;
    gap: 6px;
    margin-top: 4px;
  }
  .person-title {
    font-weight: 400;
    font-size: 17px;
    letter-spacing: 1.2px;
    color: var(--text-grey);
    margin: 0;
    white-space: nowrap;
  }
  .rule {
    flex: 1;
    height: 1.5px;
    background: var(--grey);
  }

  .contacts { position: absolute; left: 73px; top: 309px; list-style: none; margin: 0; padding: 0; }
  .contacts li {
    display: flex;
    align-items: center;
    gap: 9px;
    height: 24px;
    font-size: 17px;
    letter-spacing: 1.3px;
    color: var(--text-grey);
  }
  .contacts svg { width: 17px; height: 17px; flex: none; }
  .contacts b { color: var(--navy); font-weight: 700; }

  .address {
    position: absolute;
    left: 433px;
    top: 333px;
    font-style: normal;
    font-size: 17px;
    line-height: 24px;
    letter-spacing: 1.3px;
    color: var(--text-grey);
  }

  .back-brand {
    position: absolute;
    inset: 0;
    display: flex;
    align-items: center;
    justify-content: center;
    gap: 16px;
  }
  .back-brand .brand-dot { width: 28px; height: 28px; background: var(--gold); }
  .back-brand .brand-name { color: var(--gold); font-size: 54px; letter-spacing: 3px; }
</style>
</head>
<body>
<div class="canvas">
  <section class="card card-front">
    <svg class="side-band" viewBox="0 0 32 425" aria-hidden="true">
      <rect x="0" y="0" width="32" height="425" fill="#8f8f8f"/>
      <polygon points="0,108 16,80 32,108 32,425 0,425" fill="#1b2a52"/>
      <polyline points="0,100 16,72 32,100" fill="none" stroke="#ffffff" stroke-width="3"/>
    </svg>

    <div class="brand">
      <span class="brand-dot"></span>
      <span class="brand-name">HALEWOOD</span>
    </div>

    <div class="person">
      <p class="person-name">MORGAN HALE</p>
      <div class="title-row">
        <p class="person-title">CEO at Halewood Incorporated</p>
        <span class="rule"></span>
      </div>
    </div>

    <ul class="contacts">
      <li>
        <svg viewBox="0 0 20 20" aria-hidden="true"><circle cx="10" cy="10" r="10" fill="#1b2a52"/><path d="M5 8.5c0-2 2-3 5-3s5 1 5 3h-2.5v-1h-5v1z M6.5 10h7l1 4h-9z" fill="#fff"/><circle cx="10" cy="12" r="1.2" fill="#1b2a52"/></svg>
        (555) 214-3308
      </li>
      <li>
        <svg viewBox="0 0 20 20" aria-hidden="true"><circle cx="10" cy="10" r="10" fill="#1b2a52"/><rect x="5" y="6" width="3" height="9" fill="#fff"/><rect x="9" y="5" width="6" height="10" fill="#fff"/><rect x="10" y="7" width="4" height="2" fill="#1b2a52"/></svg>
        (555) 862-1947
      </li>
      <li>
        <svg viewBox="0 0 20 20" aria-hidden="true"><circle cx="10" cy="10" r="10" fill="#1b2a52"/><rect x="4.5" y="6.5" width="11" height="7.5" fill="none" stroke="#fff" stroke-width="1.3"/><polyline points="4.5,6.5 10,11 15.5,6.5" fill="none" stroke="#fff" stroke-width="1.3"/></svg>
        info@halewoodcb.com
      </li>
      <li>
        <svg viewBox="0 0 20 20" aria-hidden="true"><circle cx="10" cy="10" r="10" fill="#1b2a52"/><circle cx="10" cy="10" r="6" fill="none" stroke="#fff" stroke-width="1.3"/><line x1="4" y1="10" x2="16" y2="10" stroke="#fff" stroke-width="1.2"/><ellipse cx="10" cy="10" rx="2.6" ry="6" fill="none" stroke="#fff" stroke-width="1.2"/></svg>
        <span>www.<b>halewoodcb</b>.com</span>
      </li>
    </ul>

    <address class="address">
      4217 Larkspur Commons Drive<br>
      Suite 310<br>
      Mesa Verde Park, CA 91899
    </address>
  </section>

  <section class="card card-back">
    <div class="back-brand">
      <span class="brand-dot"></span>
      <span class="brand-name">HALEWOOD</span>
    </div>
  </section>
</div>
</body>
</html>
```